Book Cover Design Project

We need a book cover for a eBook on internet banking.

This eBook is meant to be an easy to read, practical book to help people understand what internet banking is, the pros and cons and cover the pure 'internet only' banks that have no branches. The intention is to help people to make informed decisions about whether to use internet banking, how to use it safely and explain in detail what 'internet only' banks are and whether they are right for them.

The cover should not look technical so that non-technical people are not scared off by the look. I have uploaded a book cover design that has the style that I am trying to portray, I have also uploaded a front cover that I created but do not think is suitable.

The cover wording layout could be something like
"Internet Banking"
"A practical guide to answer all your questions" or "The ultimate guide to internet banking" or "The Who's What's and How's of Internet Banking"
Authors name : Colin Pettifer

Industry/Entity Type

Internet

```html
<!DOCTYPE html>
<html lang="en">
<head>
<meta charset="utf-8">
<title>The Ultimate Guide to Internet Banking – Book Cover</title>
<link href="https://fonts.googleapis.com/css2?family=Arimo:wght@400;700&display=swap" rel="stylesheet">
<style>
  :root {
    --page: #ffffff;
    --title-red: #f5005a;
    --title-red-deep: #d8003c;
    --amber: #f7a100;
    --amber-deep: #e07f00;
    --sky: #12a9ec;
    --sky-deep: #0a55b8;
    --crimson: #e00000;
    --crimson-deep: #980000;
    --silver: #f2f2f2;
  }
  * { margin: 0; padding: 0; box-sizing: border-box; }
  html, body { width: 1200px; height: 1200px; overflow: hidden; background: var(--page); }
  body { font-family: "Arimo", Arial, sans-serif; }
  .canvas { position: relative; width: 1200px; height: 1200px; }

  .cover {
    position: absolute; left: 162px; top: 82px; width: 880px; height: 1040px;
    overflow: hidden;
    background: linear-gradient(180deg, #1a1a1a 0%, #5a5a5a 30%, #9a9a9a 55%, #6a6a6a 75%, #141414 100%);
  }
  .cover-swoosh { position: absolute; inset: 0; }

  .text { position: absolute; white-space: nowrap; line-height: 1; }

  .title-band {
    position: absolute; left: 0; top: 59px; width: 880px; height: 208px;
    background: linear-gradient(180deg, var(--title-red) 0%, var(--title-red) 55%, var(--title-red-deep) 100%);
  }
  .title-rule {
    position: absolute; left: 0; top: 267px; width: 880px; height: 15px;
    background: linear-gradient(180deg, var(--amber), var(--amber-deep));
  }
  .title-kicker, .title-main {
    color: var(--silver); font-weight: 700;
    text-shadow: 0 2px 0 #9a9a9a, 0 4px 6px rgba(0,0,0,.45);
  }
  .title-kicker { left: 178px; top: 85px; font-size: 60px; }
  .title-main   { left: 200px; top: 162px; font-size: 80px; }

  .author-tab {
    position: absolute; left: 654px; top: 282px; width: 206px; height: 34px;
    border-radius: 0 0 8px 8px;
    background: linear-gradient(180deg, var(--amber), var(--amber-deep));
    box-shadow: 0 3px 6px rgba(0,0,0,.4);
    color: #fff; font-weight: 700; font-size: 21px; text-align: center; line-height: 32px;
    text-shadow: 0 1px 2px rgba(0,0,0,.35);
  }

  .money-photo {
    position: absolute; left: 195px; top: 360px; width: 644px; height: 319px;
    background: linear-gradient(135deg, #d8d8d8 0%, #a8a8a8 40%, #e4e4e4 65%, #8f8f8f 100%);
  }

  .spine {
    position: absolute; left: 0; top: 0; width: 160px; height: 1040px;
    background: linear-gradient(90deg, rgba(0,0,0,.18), rgba(0,0,0,0) 85%, rgba(0,0,0,.25));
    border-right: 1px solid rgba(0,0,0,.3);
  }
  .spine-text {
    color: var(--silver);
    transform-origin: left top; transform: rotate(90deg);
    text-shadow: 0 2px 3px rgba(0,0,0,.6);
  }
  .spine-series { left: 146px; top: 336px; font-size: 50px; font-weight: 400; }
  .spine-title  { left: 87px;  top: 320px; font-size: 65px; font-weight: 400; }
  .spine-author { left: 89px;  top: 828px; font-size: 23px; font-weight: 700; }

  .tagline-shapes { position: absolute; left: 0; top: 0; width: 880px; height: 1040px; }
  .banner-text { transform: rotate(2deg); transform-origin: left top; font-weight: 700; }
  .tagline {
    color: var(--silver); font-size: 42px;
    text-shadow: 0 2px 0 #8a8a8a, 0 3px 5px rgba(0,0,0,.5);
  }
  .tagline-1 { left: 286px; top: 780px; }
  .tagline-2 { left: 458px; top: 832px; }
  .site-url, .site-company { color: #fff; text-shadow: 0 2px 3px rgba(0,0,0,.5); }
  .site-url { left: 470px; top: 915px; font-size: 32px; }
  .site-company { left: 657px; top: 957px; font-size: 19px; }
</style>
</head>
<body>
<div class="canvas">
  <div class="cover">
    <svg class="cover-swoosh" width="880" height="1040" viewBox="0 0 880 1040" aria-hidden="true">
      <defs>
        <radialGradient id="glow-top" cx="0.5" cy="0.5" r="0.5">
          <stop offset="0" stop-color="#ffffff" stop-opacity=".9"/>
          <stop offset="1" stop-color="#ffffff" stop-opacity="0"/>
        </radialGradient>
        <linearGradient id="sheen" x1="0" y1="0" x2="1" y2="0">
          <stop offset="0" stop-color="#ffffff" stop-opacity="0"/>
          <stop offset=".5" stop-color="#ffffff" stop-opacity=".35"/>
          <stop offset="1" stop-color="#ffffff" stop-opacity="0"/>
        </linearGradient>
      </defs>
      <ellipse cx="450" cy="40" rx="260" ry="30" fill="url(#glow-top)"/>
      <path d="M0 340 C250 420 520 330 880 460 L880 520 C520 400 260 480 0 420 Z" fill="url(#sheen)"/>
      <path d="M0 700 C300 620 600 720 880 640 L880 700 C600 780 300 690 0 760 Z" fill="url(#sheen)"/>
    </svg>

    <div class="title-band"></div>
    <div class="title-rule"></div>
    <div class="text title-kicker">The Ultimate Guide to</div>
    <div class="text title-main">Internet Banking</div>
    <div class="author-tab">Colin Pettifer</div>

    <div class="money-photo" role="img" aria-label="Black and white photograph of banknotes from many countries spread in a pile"></div>

    <svg class="tagline-shapes" viewBox="0 0 880 1040" aria-hidden="true">
      <defs>
        <linearGradient id="sky-band" x1="0" y1="0" x2="0" y2="1">
          <stop offset="0" stop-color="#12a9ec"/>
          <stop offset="1" stop-color="#0a55b8"/>
        </linearGradient>
        <linearGradient id="crimson-band" x1="0" y1="0" x2="0" y2="1">
          <stop offset="0" stop-color="#e00000"/>
          <stop offset="1" stop-color="#980000"/>
        </linearGradient>
      </defs>
      <polygon points="261,757 880,782 880,912 258,893" fill="url(#sky-band)"/>
      <polygon points="328,893 880,914 880,994 339,974" fill="url(#crimson-band)"/>
    </svg>
    <div class="text banner-text tagline tagline-1">The Who's What's and How's</div>
    <div class="text banner-text tagline tagline-2">to Internet Banking</div>
    <div class="text banner-text site-url">www.yourwebsiteurl.com</div>
    <div class="text banner-text site-company">Your Company Name</div>

    <div class="spine"></div>
    <div class="text spine-text spine-series">Quick Learn</div>
    <div class="text spine-text spine-title">Internet Banking</div>
    <div class="text spine-text spine-author">Colin Pettifer</div>
  </div>
</div>
</body>
</html>
```